PREMIUM AGENCY High End Business Card - A+++ Designers Wanted

** DO NOT ATTEMPT TO CONTACT ME THROUGH SEARCHING ON GOOGLE OR EMAILING ME THROUGH MY WEBSITE **

I need a fresh, contemporary business card designed using the logo attached (VOLKRANE)

I have attached the font for VOLKRANE

It must have a premium look and feel. The business card size must be STANDARD size.

You can submit either/both VERTICAL or HORIZONTAL designs.

FRONT: It must have the following sample information on

Peter Dowle
Director Operations
Mobile +61 452 000 000
Email peterdowle@volkrane.example
www.volkrane.example

The REAR of the business card must have the words

CREATE INSPIRE TOMORROW

as part of the design, in the same font (NEXA) attached.

The words do not need to be in capitals, or on the same line, please design this as you see it best working.

ADDITIONAL INFORMATION
======================

The VOLKRANE logo must be on the front of the card

I want Ultraviolet printing on the final design, to enhance either the NAME of the person OR the VOLKRANE logo OR the words on the back of the card.

Target Market(s)

Agency, Advertising Agency, Creative, Designers

Industry/Entity Type

Media

Contact Information for Business Card

Design Agency, Contemporary, Premium look and feel, High Quality

Font styles to use
Serif
Sans Serif
Other font styles liked:
• ATTACHED TO PROJECT

Requirements
Must have
• BLACK & WHITE as the primary design, and if you feel there can be a highlighted colour, then this can be used.
• The Logo ICON attached is blue, this colour must not be changed.
• I have attached the partner brand VOLKRANE MEDIA incase you need to manipulate the original files.
• ** DO NOT ATTEMPT TO CONTACT ME THROUGH SEARCHING ON GOOGLE OR EMAILING ME THROUGH MY WEBSITE **
Nice to have
• Must be Premium. I have attached some sample designs, that I like that would be a good inspiration for where this can be taken.
• My favourite design is is the SNAPFRAME2-BUSINESSCARD-TEMPLATE
Should not have
• No funny or silly standard / off the shelf designs

```html
<!DOCTYPE html>
<html lang="en">
<head>
<meta charset="utf-8">
<title>Volkrane Business Card</title>
<link rel="stylesheet" href="https://fonts.googleapis.com/css2?family=Montserrat:wght@300;400;600;700&family=Open+Sans:wght@400;600&display=swap">
<style>
  :root {
    --stage: #e8e5e0;
    --brand-blue: #2aa8e0;
    --brand-blue-deep: #1a8fca;
    --ink: #1f1f1f;
    --ink-soft: #555555;
    --paper: #ffffff;
    --paper-shade: #f1f1f1;
  }
  * { box-sizing: border-box; margin: 0; padding: 0; }
  html, body {
    width: 1200px; height: 843px; overflow: hidden;
    background: var(--stage);
  }
  .stage {
    width: 1200px; height: 843px;
    display: flex; align-items: center; justify-content: center; gap: 40px;
  }
  .card {
    width: 550px; height: 314px; position: relative;
    box-shadow: 0 10px 28px rgba(0,0,0,0.18);
  }

  /* Back of card */
  .card-back {
    background: linear-gradient(160deg, #3db4ea 0%, var(--brand-blue) 45%, var(--brand-blue-deep) 100%);
    color: var(--paper);
    display: flex; flex-direction: column; align-items: center; justify-content: center;
  }
  .back-wordmark {
    display: flex; align-items: center; gap: 14px;
  }
  .back-wordmark .mark-dot {
    width: 26px; height: 26px; border-radius: 50%; background: var(--paper);
  }
  .back-wordmark .name {
    font-family: "Montserrat", sans-serif; font-weight: 600;
    font-size: 30px; letter-spacing: 3px; color: var(--paper);
  }
  .tagline {
    position: absolute; bottom: 40px; left: 0; right: 0; text-align: center;
    font-family: "Montserrat", sans-serif; font-weight: 400;
    font-size: 12px; letter-spacing: 4px;
  }

  /* Front of card */
  .card-front {
    background: linear-gradient(180deg, var(--paper) 0%, var(--paper) 70%, var(--paper-shade) 100%);
  }
  .front-wordmark {
    position: absolute; top: 82px; left: 0; right: 0;
    display: flex; align-items: center; justify-content: center; gap: 16px;
  }
  .front-wordmark .mark-dot {
    width: 34px; height: 34px; border-radius: 50%; background: var(--brand-blue);
  }
  .front-wordmark .name {
    font-family: "Montserrat", sans-serif; font-weight: 600;
    font-size: 40px; letter-spacing: 5px; color: var(--ink);
  }
  .rule {
    position: absolute; height: 1.5px; background: var(--brand-blue);
  }
  .rule-top { top: 190px; left: 26px; width: 250px; }
  .rule-bottom { top: 272px; left: 280px; width: 244px; }
  .identity {
    position: absolute; top: 198px; left: 0; right: 0;
    display: flex; align-items: center; justify-content: center; gap: 12px;
  }
  .identity .person {
    font-family: "Montserrat", sans-serif; font-weight: 600;
    font-size: 18px; letter-spacing: 1.5px; color: var(--brand-blue);
  }
  .identity .divider { width: 1.5px; height: 20px; background: var(--ink-soft); }
  .identity .role {
    font-family: "Open Sans", sans-serif; font-weight: 600;
    font-size: 14px; color: var(--ink);
  }
  .contacts {
    position: absolute; top: 240px; left: 0; right: 0;
    display: flex; justify-content: center; gap: 14px;
    font-family: "Open Sans", sans-serif; font-size: 11.5px; color: var(--ink-soft);
  }
  .contact { display: flex; align-items: center; gap: 5px; }
  .contact svg { width: 13px; height: 13px; flex: none; }
</style>
</head>
<body>
<main class="stage">
  <section class="card card-back" aria-label="Card back">
    <div class="back-wordmark">
      <span class="mark-dot"></span>
      <span class="name">VOLKRANE MEDIA</span>
    </div>
    <p class="tagline">CREATE · INSPIRE · TOMORROW</p>
  </section>

  <section class="card card-front" aria-label="Card front">
    <div class="front-wordmark">
      <span class="mark-dot"></span>
      <span class="name">VOLKRANE</span>
    </div>
    <div class="rule rule-top"></div>
    <div class="identity">
      <span class="person">PETER DOWLE</span>
      <span class="divider"></span>
      <span class="role">Director Operations</span>
    </div>
    <div class="contacts">
      <span class="contact">
        <svg viewBox="0 0 14 14" aria-hidden="true"><rect x="3.5" y="1" width="7" height="12" rx="1.2" fill="none" stroke="#2aa8e0" stroke-width="1.4"/><circle cx="7" cy="11" r="0.8" fill="#2aa8e0"/></svg>
        +61 452 000 000
      </span>
      <span class="contact">
        <svg viewBox="0 0 14 14" aria-hidden="true"><rect x="1" y="3" width="12" height="8.5" fill="#2aa8e0"/><path d="M1 3 L7 8 L13 3" fill="none" stroke="#ffffff" stroke-width="1"/></svg>
        peterdowle@volkrane.example
      </span>
      <span class="contact">
        <svg viewBox="0 0 14 14" aria-hidden="true"><circle cx="7" cy="7" r="6" fill="#2aa8e0"/><ellipse cx="7" cy="7" rx="2.5" ry="6" fill="none" stroke="#ffffff" stroke-width="0.9"/><line x1="1" y1="7" x2="13" y2="7" stroke="#ffffff" stroke-width="0.9"/></svg>
        www.volkrane.example
      </span>
    </div>
    <div class="rule rule-bottom"></div>
  </section>
</main>
</body>
</html>
```